Business Card Design

Business Card for professional consulting firm working with large financial institutions.

Target Market(s)

Executive buyers

Industry/Entity Type

Banking

Contact Information for Business Card

Mild creativity wanted. Not boring, but do elaborate artwork.

Font styles to use
Serif
Sans Serif

Colors

Designer to choose colors to be used in the design.

Requirements
Must have
• Standard business card features - company name, individual name, telephone, website, email, locations.
Nice to have
• Two colors
Should not have
• too many colors, fancy printing, cartoons.

```html
<!DOCTYPE html>
<html lang="en">
<head>
<meta charset="utf-8">
<title>Harbridge Business Card</title>
<link rel="stylesheet" href="https://fonts.googleapis.com/css2?family=Open+Sans:wght@400;600;700&display=swap">
<style>
  :root {
    --backdrop: #d1d2d4;
    --card: #ffffff;
    --panel: #58585a;
    --ink: #231f20;
    --ink-soft: #555557;
    --rule: #6d6e70;
  }
  * { margin: 0; padding: 0; box-sizing: border-box; }
  html, body { width: 1200px; height: 999px; overflow: hidden; }
  body { background: var(--backdrop); position: relative; font-family: "Open Sans", Arial, sans-serif; color: var(--ink); }
  .card {
    position: absolute;
    background: var(--card);
    border-radius: 18px;
    overflow: hidden;
    box-shadow: 0 14px 18px -10px rgba(0,0,0,0.45);
  }
  .card-front { left: 287px; top: 94px; width: 621px; height: 355px; }
  .card-back { left: 285px; top: 532px; width: 630px; height: 360px; }
  .card-art { position: absolute; inset: 0; }
  .brand-name {
    position: absolute; left: 0; width: 708px; top: 144px;
    text-align: center;
    font-family: "Open Sans", Arial, sans-serif;
    font-size: 40px; font-weight: 600; letter-spacing: 1px;
    color: var(--ink);
  }
  .front-url {
    position: absolute; left: 0; width: 696px; top: 257px;
    text-align: center; font-size: 13px; font-weight: 700;
    letter-spacing: 0.5px; color: var(--ink);
  }
  .person {
    position: absolute; left: 300px; width: 348px; top: 40px; text-align: center;
  }
  .person-name { font-size: 28px; font-weight: 700; letter-spacing: 1px; line-height: 40px; }
  .person-role { font-size: 18px; font-weight: 600; color: var(--ink-soft); letter-spacing: 1px; line-height: 24px; }
  .person-rule {
    position: absolute; left: 367px; top: 119px; width: 218px; height: 3px;
    background: linear-gradient(90deg, transparent, var(--rule) 12%, var(--rule) 88%, transparent);
  }
  .contact-list { list-style: none; }
  .contact-item { position: absolute; left: 354px; display: flex; align-items: center; }
  .contact-icon { width: 40px; height: 40px; flex: none; }
  .contact-text { margin-left: 18px; font-size: 13.5px; font-weight: 700; line-height: 17px; }
</style>
</head>
<body>

<section class="card card-front" aria-label="Card front">
  <svg class="card-art" width="621" height="355" viewBox="0 0 621 355" role="img" aria-label="Dark grey panel with an abstract crossing-line pattern">
    <rect width="621" height="355" fill="var(--panel)"/>
    <circle cx="379.5" cy="177.5" r="273.5" fill="var(--card)"/>
    <rect x="379.5" width="241.5" height="355" fill="var(--card)"/>
  </svg>
  <div class="brand-name">Harbridge</div>
  <div class="front-url">WWW.YOURCOMPANY.COM</div>
</section>

<section class="card card-back" aria-label="Card back">
  <svg class="card-art" width="630" height="360" viewBox="0 0 630 360" role="img" aria-label="Dark grey panel with an abstract crossing-line pattern">
    <rect width="630" height="360" fill="var(--panel)"/>
    <circle cx="381.5" cy="180" r="273.5" fill="var(--card)"/>
    <rect x="381.5" width="248.5" height="360" fill="var(--card)"/>
  </svg>

  <div class="person">
    <div class="person-name">MARCUS. H</div>
    <div class="person-role">DIRECTOR</div>
  </div>
  <div class="person-rule"></div>

  <ul class="contact-list">
    <li class="contact-item" style="top:143px">
      <svg class="contact-icon" viewBox="0 0 40 40"><circle cx="20" cy="20" r="20" fill="var(--panel)"/><path d="M20 9c-4.4 0-7.5 3.2-7.5 7.3 0 5.2 7.5 14 7.5 14s7.5-8.8 7.5-14C27.5 12.2 24.4 9 20 9z" fill="#fff"/><circle cx="20" cy="16.5" r="2.8" fill="var(--panel)"/></svg>
      <span class="contact-text">FIRST ADDRESS<br>SECOND &nbsp;ADDRESS</span>
    </li>
    <li class="contact-item" style="top:191px">
      <svg class="contact-icon" viewBox="0 0 40 40"><circle cx="20" cy="20" r="20" fill="var(--panel)"/><rect x="10" y="13" width="20" height="14" fill="none" stroke="#fff" stroke-width="2"/><path d="M10 13l10 8 10-8M10 27l7-6M30 27l-7-6" fill="none" stroke="#fff" stroke-width="2"/></svg>
      <span class="contact-text">YOUR@YOURMAIL.COM</span>
    </li>
    <li class="contact-item" style="top:238px">
      <svg class="contact-icon" viewBox="0 0 40 40"><circle cx="20" cy="20" r="20" fill="var(--panel)"/><path d="M14 10l4 5-2.5 3c1.5 3 3.5 5 6.5 6.5l3-2.5 5 4-2.5 4C19 29 11 21 10 13.5z" fill="#fff"/></svg>
      <span class="contact-text">+0 123 456 789<br>+0 123 456 789</span>
    </li>
    <li class="contact-item" style="top:286px">
      <svg class="contact-icon" viewBox="0 0 40 40"><circle cx="20" cy="20" r="20" fill="var(--panel)"/><g fill="none" stroke="#fff" stroke-width="1.8"><circle cx="20" cy="20" r="9.5"/><ellipse cx="20" cy="20" rx="4" ry="9.5"/><path d="M10.5 20h19M12 15h16M12 25h16"/></g></svg>
      <span class="contact-text" style="margin-left:22px">WWW.YOURCOMPANY.COM</span>
    </li>
  </ul>
</section>

</body>
</html>
```